Create for a public aquarium, create the face page of the program of the animations of the french w

We operate a public aquarium. We are currently working on the edition of the french flyer concernant winter holidays. The size is 100 mm (wide) x 210 mm (high) and the text must be in french Our request concerned the graphic Creation of the front of the leaflet (only one side) as well as the layout of all the information concernant the events years the activities The logo and the adress must APPEAR one flyer we add Several files as attachments to help create this page: - logos in color and black and white - a small brief of what we want - the texts you That you need to include in The leaflet has the leaflet is distributed in shops, restaurants, places of passage. It is significant That Graphically graphic design Attracts the eye and makes you want to take it in hand and read it. It is not Necessary to cover the overload with too many pictures, it is Necessary to find the right dosage. To help you in your establishment, You Could visit our website: oceanoriumdelisle.fr

Hello, We have already received several projects but for the moment we are not satisfied by the different proposals. We hope for more colorful and fun projects In general, we have the impression that the texts are superimposed on the background images. The layout must communicate between text and image. As we mention in the brief, we are reminded of the fact that we have different types of information to be presented on the front of the leaflet. Your winter vacation at the Brelot aquarium Then, the central part of the leaflet presenting the animations. 3 types of different animations: - First animations that we offer each holiday: Every day, animations commented with the tactile basin Every afternoon, feedings commented on our animals - Second Animations that we have created specially for the winther holiday: The visits Free Guided Tours February 7th, 14th, 21st & 28th at 2pm Scientific workshops for children aged 6 to 12 February 8th, 15th, 22nd and March 1st from 2pm to 5pm - 16 € per child Activities of the little biologist - history Seaweed February 16 & 23 from 10am to 12:30 pm and from 1:30 pm to 5:30 pm - free Third Valentine's Day at the aquarium February 14th at 7:30 pm - 71 € per person Culinary demo with Gaspard MOLINEAU on the theme of Saint-Jacques February 21 at 17:30 - 29 € per person WE EXPECT A REAL GRAPHIC WORK TO HIGHLIGHT IN DIFFERENT WAY THESE THREE CATEGORIES OF ANIMATIONS. THEY SHOULD NOT BE PRESENTED AS A LIST. Concerning the footer, all of the information about oceanoriumdelisle.fr is also important because we are looking for more information about our activities. We will certainly extend the contest to have new projects. Thanks Lucas

Hello, We have already received several projects but for the moment we are not satisfied by the different proposals. We hope for more colorful and fun projects In general, we have the impression that the texts are superimposed on the background images. The layout must communicate between text and image. As we mention in the brief, we are reminded of the fact that we have different types of information to be presented on the front of the leaflet. Your winter vacation at the Brelot aquarium Then, the central part of the leaflet presenting the animations. 3 types of different animations: - First animations that we offer each holiday: Every day, animations commented with the tactile basin Every afternoon, feedings commented on our animals - Second Animations that we have created specially for the winther holiday: The visits Free Guided Tours 7, 14, 21 & amp; February 28 at 2 pm Scientific workshops for children aged 6 to 12 February 8, 15, 22 & amp; amp; March 1st from 2pm to 5pm - 16 € per child The animations of the little biologist - algae story Les 16 & amp; amp; amp; February 23 from 10h to 12h30 and from 13h30 to 17h30 - free of charge Saint Valentine's Day at the Aquarium 14th February at 7.30pm - 71 € per person Culinary Demo with Gaspard MOLINEAU on the theme of Saint-Jacques February 21 at 17:30 - 29 € per person WE EXPECT TO REAL GRAPHIC WORK TO HIGHLIGHT IN DIFFERENT WAY THESE THREE CATEGORIES OF ANIMATIONS. THEY SHOULD NOT BE PRESENTED AS A LIST. Concerning the footer, all of the information about oceanoriumdelisle.fr is also important because we are looking for more information about our activities. We will certainly extend the contest to have new projects. Thanks Lucas

Reason: Hello, We have already received several projects but we are not satisfied by the different proposals. We hope for more colorful and fun projects In general, we have the impression that the texts are superimposed on the background images. The layout must communicate between text and image. As we mention in the brief, we are reminded of the fact that we have different types of information to be presented on the front of the leaflet. The winter holiday at the Brelot aquarium Then, the central part of the leaflet presenting the animations. 3 different types of animations: - Every day, animations commented on the tactile basin Every afternoon, feedings commented on our animals - Second Animations that we have created specially for the winther holiday: The visits free guided tours February 7, 14, 21 and 28 at 2 pm Scientific workshops for children aged 6 to 12 8, 15, 22 February and 1 March from 2 to 5 pm - € 16 per child Activities of the little biologist - history Seaweed February 16 and 23 from 10am to 12:30 pm and from 13:30 to 17:30 - free Third Valentine's Day at the aquarium February 14th at 7:30 pm - 71 € per person Culinary demo with Gaspard MOLINEAU on the theme of Saint-Jacques February 21 at 17:30 - 29 € per person It's important to have a special graphism ans layout for this third part. indeed, the first animation concerns the Valentine's day that we organize (dinner with the caterer in the aquarium) and the second is a culinary animation with a great chef. WE EXPECT A REAL GRAPHIC WORK TO HIGHLIGHT IN DIFFERENT WAY THESE THREE CATEGORIES OF ANIMATIONS. THEY SHOULD NOT BE PRESENTED AS A LIST. Concerning the footer, all of the information about oceanoriumdelisle.fr is also important because we are looking for more information about our activities. Thanks

Target Market(s)

General public Customer Family

Font styles to use
Serif

Requirements
Must have
• The leaflet is a distributed in-shops, restaurants, places of passage. It is significant That Graphically graphic design Attracts the eye and makes you want to take it in hand and read it. It is not Necessary to cover the overload with too many pictures, it is Necessary to find the right dosage.

```html
<!DOCTYPE html>
<html lang="fr">
<head>
<meta charset="utf-8">
<title>Vacances d'hiver – Aquarium de Brelot</title>
<link href="https://fonts.googleapis.com/css2?family=Oswald:wght@300;400;500&display=swap" rel="stylesheet">
<style>
  :root {
    --page-bg: #e9e9e9;
    --paper: #ffffff;
    --brand-blue: #2f6fb6;
    --brand-green: #1e9e49;
    --ink: #222222;
    --info-bg-top: #e2e4e4;
    --info-bg-bottom: #f2f2f2;
    --rule: #9a9a9a;
  }
  * { margin: 0; padding: 0; box-sizing: border-box; }
  html, body { width: 1200px; height: 1000px; overflow: hidden; }
  body {
    background: var(--page-bg);
    font-family: "Oswald", "Arial Narrow", sans-serif;
    font-weight: 300;
    color: var(--ink);
    position: relative;
  }
  .flyer {
    position: absolute; left: 218px; top: 74px;
    width: 410px; height: 864px;
    background: var(--paper);
  }
  .hero {
    position: absolute; left: 0; top: 0; width: 410px; height: 250px;
    background:
      radial-gradient(ellipse 62% 48% at 62% 62%, rgba(70,150,150,0.95) 0%, rgba(48,110,112,0.7) 45%, rgba(30,60,55,0) 100%),
      radial-gradient(ellipse 55% 40% at 70% 22%, rgba(120,125,110,0.75) 0%, rgba(60,70,60,0) 100%),
      linear-gradient(180deg, #111a17 0%, #1f332d 45%, #2c4a36 80%, #1b2b20 100%);
  }
  .hero-title {
    position: absolute; left: 14px; top: 6px; width: 300px;
    color: #fff; font-size: 32px; line-height: 42px; font-weight: 300;
    letter-spacing: -0.3px;
  }
  .thumbs { position: absolute; left: 0; top: 250px; height: 89px; width: 410px; display: flex; }
  .thumb { height: 100%; }
  .thumb--reptile {
    width: 122px;
    background:
      radial-gradient(circle at 54% 58%, #d9a21c 0%, #a8741a 12%, rgba(120,110,60,0) 26%),
      linear-gradient(150deg, #a8a56a 0%, #7c7a44 45%, #4a4626 100%);
  }
  .thumb--piranha {
    width: 147px;
    background:
      radial-gradient(ellipse 45% 30% at 50% 68%, #d2443a 0%, rgba(200,70,60,0) 100%),
      radial-gradient(ellipse 50% 40% at 50% 45%, #c8c6c0 0%, rgba(160,160,150,0) 100%),
      linear-gradient(135deg, #5e6f66 0%, #7b8a80 50%, #3f4a45 100%);
  }
  .thumb--lionfish {
    width: 141px;
    background:
      radial-gradient(ellipse 55% 50% at 65% 45%, #8a7ed0 0%, rgba(110,95,180,0) 100%),
      linear-gradient(135deg, #1f2a66 0%, #3e4aa0 45%, #20224a 100%);
  }
  .bands { position: absolute; left: 0; top: 339px; width: 410px; height: 85px; display: flex; }
  .band {
    display: flex; align-items: center; justify-content: center; text-align: center;
    color: #fff; font-size: 16px; line-height: 21px;
  }
  .band--daily { width: 205px; background: var(--brand-blue); }
  .band--afternoon { width: 205px; background: var(--brand-green); }
  .events {
    position: absolute; left: 0; top: 424px; width: 410px; height: 208px;
    background: linear-gradient(180deg, var(--info-bg-top), var(--info-bg-bottom));
  }
  .events-side { position: absolute; left: 23px; top: 13px; width: 134px; }
  .event-small { font-size: 10.5px; line-height: 13.5px; color: var(--ink); padding-bottom: 7px; margin-bottom: 7px; border-bottom: 1px solid var(--rule); }
  .event-small:last-child { border-bottom: none; }
  .events-main { position: absolute; left: 180px; top: 11px; width: 214px; }
  .event-big { font-size: 15.5px; line-height: 21px; }
  .event-big--valentine { color: var(--brand-blue); padding-bottom: 12px; border-bottom: 1px solid var(--rule); margin-bottom: 13px; }
  .event-big--demo { color: var(--brand-green); }
  .brand-block {
    position: absolute; left: 0; top: 660px; width: 410px;
    display: flex; justify-content: center;
  }
  .brand-name { display: flex; align-items: center; gap: 9px; color: var(--brand-blue); font-size: 30px; font-weight: 500; white-space: nowrap; }
  .brand-dot { width: 14px; height: 14px; border-radius: 50%; background: var(--brand-green); flex: none; }
  .contact {
    position: absolute; left: 0; top: 787px; width: 410px; text-align: center;
    font-size: 10.5px; line-height: 14px;
  }
  .web-bar {
    position: absolute; left: 0; top: 832px; width: 410px; height: 19px;
    background: var(--brand-blue); color: #fff; text-align: center;
    font-size: 12.5px; line-height: 19px;
  }
  .logo-showcase {
    position: absolute; left: 720px; top: 768px; width: 420px;
    display: flex; align-items: center; justify-content: center; gap: 14px;
    color: var(--brand-blue); font-size: 46px; font-weight: 500; line-height: 1;
    white-space: nowrap;
  }
  .logo-showcase .brand-dot { width: 24px; height: 24px; }
</style>
</head>
<body>
  <main class="flyer">
    <section class="hero" role="img" aria-label="Photo d'un grand poisson bleu-vert nageant dans un bassin">
      <h1 class="hero-title">Vos vacances d’hiver à l’aquarium de Brelot Du 4 février au 5 mars 2017</h1>
    </section>
    <div class="thumbs">
      <div class="thumb thumb--reptile" role="img" aria-label="Gros plan sur l'œil d'un crocodile"></div>
      <div class="thumb thumb--piranha" role="img" aria-label="Piranha au ventre rouge"></div>
      <div class="thumb thumb--lionfish" role="img" aria-label="Poisson-lion dans un bassin bleu"></div>
    </div>
    <div class="bands">
      <p class="band band--daily">Tous les jours, animations<br>commentées<br>au bassin tactile</p>
      <p class="band band--afternoon">Tous les après-midis,<br>nourrissages<br>commentés de nos animaux</p>
    </div>
    <section class="events">
      <div class="events-side">
        <p class="event-small">Les visites guidées gratuites<br>Les 7, 14, 21 &amp; 28 février à 14h</p>
        <p class="event-small">Les ateliers scientifiques pour les enfants de 6 à 12 ans<br>Les 8, 15, 22 février &amp; 1er mars de 14h à 17h - 16 € par enfant</p>
        <p class="event-small">Les animations du petit biologiste - histoire d’algues<br>Les 16 &amp; 23 février de 10h à 12h30 et de 13h30 à 17h30 - gratuit</p>
      </div>
      <div class="events-main">
        <p class="event-big event-big--valentine">La Saint-Valentin à l’aquarium<br>Le 14 février à 19h30 - 71 € par personne</p>
        <p class="event-big event-big--demo">Démo culinaire avec Gaspard MOLINEAU sur le thème de la Saint-Jacques Le 21 février à 17h30 - 29 € par personne</p>
      </div>
    </section>
    <div class="brand-block">
      <div class="brand-name"><span class="brand-dot"></span>Aquarium de Brelot</div>
    </div>
    <p class="contact">Aquarium de Brelot · 14 rue Émile FERRAND · 56990 BRELOT · 02 00 41 58 36<br>Ouvert tous les jours de 10h à 18h - Direction Parc de la Baie - Casino/jeux</p>
    <p class="web-bar">Retrouvez toutes les informations sur oceanoriumdelisle.fr</p>
  </main>
  <div class="logo-showcase"><span class="brand-dot"></span>Aquarium de Brelot</div>
</body>
</html>
```